Modern Employee Handbook Cover Design Needed

I need help. I am designing a 50+ page Employee Handbook and want a great cover design. I'm looking for a great cover because our company has changed so much in the past years since the last handbook was published and I want to signify and celebrate all the positive things we have done. It may not seem like such a big deal but I'm trying to make a big impact.

I'm looking for something interesting. Employee Handbooks are the most boring things int he world but I don't ours to LOOK that way. I want creative, modern, slick, clean, whatever you want that would make someone want to look at (even if it is for a second). It does NOT need to even be called an Employee Handbook (I'm really open to ideas)

This will be a typical 8.5 x 11 book format. 70% of our employees are under the age of 40 and are in CA, MA, FL, and IN.

The final design should communicate that we are not the same company we were a few years ago but instead we are more modern and current.

Target Market(s)

Most of our employees are under 40 years old. They are well educated. We are a national company with employees in CA, MA, FL and IN

Industry/Entity Type

Education

Font styles to use
Serif
Sans Serif
Other font styles liked:
• I like the fonts used by velmo but am open to ANY fonts.

Requirements
Must have
• Modern, up to date designs, unexpected, unique, cool, etc...
Should not have
• I don't like the typical teamwork images, world and globe things, or tree supporting branch type things that Human Resources and Employee Handbooks often is represented by in print. They are so boring to me. https://www.trelvasearch.com/search?q=human+resources+handbook&source=lnms&tbm=isch&sa=X&ved=0ahUKEwjl1oWHt67RAhULw1QKHWTaB0oQ_AUICCgB&biw=1920&bih=950
• No stick figures standing in a row or shaking hands. Stuff like that is so old.
• Our clients are young adults with Autism but I don't want puzzle pieces which is a universal symbol of Autism.

```html
<!DOCTYPE html>
<html lang="en">
<head>
<meta charset="UTF-8">
<title>Employee Handbook Cover</title>
<link rel="stylesheet" href="https://fonts.googleapis.com/css2?family=Open+Sans:wght@400;600;700&display=swap">
<style>
  :root {
    --page-bg: #efece7;
    --cover-bg: #dcdddf;
    --navy-deep: #061823;
    --navy-teal: #0b2c3a;
    --navy-black: #02080d;
    --gold: #c8a53c;
    --gold-soft: #d9cfae;
    --gold-faint: #e3dfd2;
    --white: #f4f5f6;
    --ink: #2b2f33;
  }
  * { margin: 0; padding: 0; box-sizing: border-box; }
  html, body {
    width: 1200px;
    height: 789px;
    overflow: hidden;
    background: var(--page-bg);
    font-family: "Open Sans", Arial, sans-serif;
  }
  .cover {
    position: absolute;
    left: 360px;
    top: 20px;
    width: 480px;
    height: 750px;
    background: var(--cover-bg);
    overflow: hidden;
    box-shadow: 0 6px 18px rgba(0,0,0,0.12);
  }
  .cover-top-band {
    position: absolute;
    left: 0; top: 0;
    width: 100%; height: 22px;
    background: linear-gradient(90deg, var(--navy-teal), var(--navy-deep));
  }
  .cover-top-rule {
    position: absolute;
    left: 0; top: 26px;
    width: 100%; height: 3px;
    background: var(--navy-deep);
  }
  .cover-url {
    position: absolute;
    left: 14px; top: 50px;
    font-size: 12px;
    font-weight: 400;
    color: var(--ink);
    letter-spacing: 0.2px;
  }
  .ornament-area {
    position: absolute;
    border-radius: 8px;
    background: linear-gradient(135deg, var(--gold-soft), var(--gold-faint));
    opacity: 0.55;
  }
  .ornament-area--top { left: 318px; top: 62px; width: 126px; height: 165px; }
  .ornament-area--bottom { left: 18px; top: 568px; width: 108px; height: 140px; }
  .title-band {
    position: absolute;
    left: 0; top: 300px;
    width: 100%; height: 222px;
    background: linear-gradient(90deg, var(--navy-teal) 0%, var(--navy-deep) 55%, var(--navy-black) 100%);
    border-top: 5px solid var(--gold);
    border-bottom: 5px solid var(--gold);
    display: flex;
    flex-direction: column;
    align-items: center;
    justify-content: center;
  }
  .title {
    color: var(--white);
    font-weight: 700;
    font-size: 52px;
    line-height: 64px;
    letter-spacing: 3px;
    text-align: center;
  }
  .title span { display: block; }
  .author-name {
    position: absolute;
    left: 0; top: 716px;
    width: 100%;
    text-align: center;
    font-size: 17px;
    font-weight: 600;
    color: var(--ink);
    letter-spacing: 0.5px;
  }
</style>
</head>
<body>
  <main class="cover">
    <div class="cover-top-band"></div>
    <div class="cover-top-rule"></div>
    <p class="cover-url">www.staffguidebook.net</p>

    <div class="ornament-area ornament-area--top" role="img" aria-label="Decorative gold outline ornament"></div>

    <section class="title-band">
      <h1 class="title"><span>EMPLOYEE</span><span>HANDBOOK</span></h1>
    </section>

    <div class="ornament-area ornament-area--bottom" role="img" aria-label="Decorative gold outline ornament"></div>

    <p class="author-name">AUTHOR NAME</p>
  </main>
</body>
</html>
```